Lien Post Card - (5.5 x 8.5)

FRONT OF POSTCARD
Is a Property Lien Putting Your Home at Risk?
HOA Liens • Tax Liens • Municipal Charges • Other Property-Related Liens
You may have options to resolve outstanding liens and protect your home.
A Refinance or Home Equity Line of Credit (HELOC) may help you:
✔ Pay off qualifying liens
✔ Consolidate debt into one manageable payment
✔ Access your home's equity
✔ Improve your financial flexibility
✔ Avoid additional penalties, fees, or collection actions
Don't wait until the situation becomes more difficult.
Call today for a confidential review of your options.
Bluegate Lending Partners, Inc.
(800) 647-2915 x 42
www.bluegatelendco.com
NMLS #381640
BACK OF POSTCARD
Your Home Equity Could Be the Solution
If you have received notices regarding:
• Delinquent Property Taxes
• HOA or Condo Association Assessments
• Municipal Utility Liens
• Special Assessments
• Other Property-Related Obligations
You may qualify for financing options designed to help satisfy those obligations and bring your property current.
Our experienced mortgage professionals can review your situation and discuss available programs, including:
• Cash-Out Refinancing
• Home Equity Lines of Credit (HELOCs)
• Home Equity Loans
• Debt Consolidation Solutions
Free Consultation • No Obligation
Contact Marcus Delaney today at (800) 647-2915 x42 or mdelaney@bluegatelendco.com (NMLS #57308)

```html
<!DOCTYPE html>
<html lang="en">
<head>
<meta charset="utf-8">
<title>Lien Postcard – Bluegate Lending Partners</title>
<link rel="stylesheet" href="https://fonts.googleapis.com/css2?family=Oswald:wght@500;600;700&family=Figtree:ital,wght@0,400;0,500;0,600;0,700;0,800;1,700;1,800&display=swap">
<style>
  :root {
    --navy: #0d4f7e;
    --navy-deep: #0a3f68;
    --blue: #1690cf;
    --green: #9dc63b;
    --lime: #c5dc4a;
    --cream: #ede5b8;
    --cream-light: #f5efcf;
    --gold: #b8a53a;
    --ink: #1e2a35;
    --white: #ffffff;
    --stage: #e2e2e2;
  }
  * { box-sizing: border-box; margin: 0; padding: 0; }
  html, body { width: 1143px; height: 1200px; overflow: hidden; }
  body { background: var(--stage); font-family: "Figtree", sans-serif; color: var(--ink); position: relative; }

  .postcard { position: absolute; left: 198px; width: 747px; height: 498px; background: var(--white); overflow: hidden; }
  .postcard--front { top: 71px; }
  .postcard--back { top: 616px; }

  .brand { position: absolute; display: flex; align-items: center; gap: 8px; }
  .brand__dot { width: 16px; height: 16px; border-radius: 50%; background: var(--navy); flex: none; }
  .brand__name { font-family: "Figtree", sans-serif; font-weight: 800; font-size: 17px; line-height: 1.1; color: var(--navy); }

  /* front */
  .front__header { position: absolute; left: 0; top: 0; width: 100%; height: 135px; background: linear-gradient(90deg, #fff 55%, #eef1f3); }
  .front__header .brand { left: 40px; top: 44px; width: 170px; }
  .headline { position: absolute; left: 232px; top: 30px; font-family: "Oswald", sans-serif; font-weight: 700; font-size: 42px; line-height: 44px; letter-spacing: 0.2px; text-transform: uppercase; color: var(--navy); white-space: nowrap; transform: scaleX(0.92); transform-origin: left top; }
  .headline span { color: var(--blue); display: block; }
  .lien-band { position: absolute; left: 0; top: 135px; width: 100%; height: 36px; background: var(--green); display: flex; align-items: center; justify-content: center; font-weight: 800; font-style: italic; font-size: 17.5px; color: var(--navy-deep); }
  .front__photo { position: absolute; left: 0; top: 171px; width: 373px; height: 248px; background: linear-gradient(135deg, #e8e6e3 0%, #b8bcc2 45%, #5d7894 70%, #d8d4d0 100%); }
  .front__copy { position: absolute; left: 396px; top: 184px; width: 335px; }
  .front__intro { font-size: 13.4px; line-height: 17px; max-width: 305px; }
  .front__sub { margin-top: 12px; font-weight: 700; font-size: 15px; line-height: 17px; color: var(--navy); }
  .checklist { list-style: none; }
  .front__copy .checklist { margin-top: 8px; }
  .front__copy .checklist li { font-size: 13px; line-height: 20px; display: flex; align-items: center; gap: 8px; white-space: nowrap; }
  .tick { width: 11px; height: 11px; flex: none; }
  .front__footer { position: absolute; left: 0; top: 419px; width: 100%; height: 79px; background: linear-gradient(90deg, var(--navy-deep), #0b66a0); }
  .front__contact { position: absolute; left: 0; top: 461px; width: 100%; text-align: center; font-weight: 700; font-size: 14.8px; color: var(--white); }
  .cta { position: absolute; left: 46px; top: 384px; width: 655px; height: 67px; background: linear-gradient(90deg, #efe6b6, #f7f1d4 50%, #ebe0ad); text-align: center; padding-top: 14px; }
  .cta__lead { font-size: 12.6px; font-weight: 500; text-transform: uppercase; color: var(--navy); }
  .cta__main { font-size: 19.8px; font-weight: 800; text-transform: uppercase; color: var(--navy); margin-top: 2px; letter-spacing: 0.2px; }

  /* back */
  .back__photo { position: absolute; left: 0; top: 0; width: 373px; height: 124px; background: linear-gradient(180deg, #7b6a8a 0%, #a8857f 45%, #8b5a3c 70%, #3a2a2a 100%); }
  .back__panel { position: absolute; left: 0; top: 124px; width: 373px; height: 178px; background: linear-gradient(180deg, var(--navy-deep), #0e4f80); padding: 14px 20px 0 33px; color: var(--white); overflow: hidden; }
  .back__title { display: inline-block; font-family: "Oswald", sans-serif; font-weight: 600; font-size: 20px; line-height: 24px; text-transform: uppercase; color: var(--cream); white-space: nowrap; transform: scaleX(0.82); transform-origin: left top; }
  .back__title span { color: var(--lime); }
  .back__lead { margin-top: 9px; font-weight: 700; font-size: 11.8px; }
  .notices { list-style: none; margin-top: 1px; }
  .notices li { font-size: 10.6px; line-height: 14.3px; position: relative; padding-left: 11px; }
  .notices li::before { content: ""; position: absolute; left: 1px; top: 6px; width: 3px; height: 3px; border-radius: 50%; background: var(--lime); }
  .back__close { margin-top: 6px; font-size: 11.6px; line-height: 14px; font-weight: 500; }
  .back__programs { position: absolute; left: 0; top: 302px; width: 373px; height: 117px; background: var(--cream); padding: 12px 20px 0 33px; }
  .programs__lead { font-weight: 700; font-size: 11.7px; line-height: 14px; color: var(--navy); max-width: 305px; }
  .programs__grid { margin-top: 7px; display: grid; grid-template-columns: 170px 150px; row-gap: 4px; }
  .programs__grid li { list-style: none; display: flex; align-items: flex-start; gap: 6px; font-size: 10.9px; line-height: 12px; color: var(--navy); }
  .programs__grid .tick { margin-top: 1px; }
  .back__contact-band { position: absolute; left: 0; top: 419px; width: 373px; height: 79px; background: linear-gradient(90deg, #c2ae40, var(--gold)); }
  .headshot { position: absolute; left: 26px; top: 406px; width: 72px; height: 74px; border: 2px solid var(--white); background: linear-gradient(180deg, #d9d9d9, #8f8f8f); }
  .contact { position: absolute; left: 112px; top: 429px; color: var(--white); }
  .contact__lead { font-size: 8.3px; }
  .contact__phone { display: flex; align-items: center; gap: 3px; font-weight: 700; font-size: 15px; line-height: 18px; margin-top: 2px; }
  .contact__mail { display: flex; align-items: center; gap: 5px; font-weight: 600; font-size: 10px; margin-top: 1px; }
  .contact__nmls { font-size: 8px; margin-top: 3px; }
  .badge { position: absolute; left: 269px; top: 394px; width: 90px; height: 90px; border-radius: 50%; background: var(--navy-deep); border: 2px solid var(--white); text-align: center; color: var(--white); padding-top: 12px; }
  .badge__free { font-family: "Oswald", sans-serif; font-weight: 700; font-size: 24px; line-height: 26px; }
  .badge__consult { font-family: "Oswald", sans-serif; font-weight: 500; font-size: 11.5px; color: var(--lime); line-height: 14px; }
  .badge__no { font-family: "Oswald", sans-serif; font-weight: 500; font-size: 9px; margin-top: 5px; }
  .back__mail-side .brand { left: 400px; top: 76px; width: 170px; }
  .stamp-box { position: absolute; left: 646px; top: 21px; width: 78px; height: 80px; background: #d1d2d4; }
</style>
</head>
<body>
  <svg width="0" height="0" style="position:absolute" aria-hidden="true">
    <symbol id="tick" viewBox="0 0 12 12"><circle cx="6" cy="6" r="6" fill="currentColor"/><path d="M3.3 6.2l1.8 1.8 3.6-3.8" fill="none" stroke="#fff" stroke-width="1.6" stroke-linecap="round" stroke-linejoin="round"/></symbol>
  </svg>

  <section class="postcard postcard--front">
    <header class="front__header">
      <div class="brand"><span class="brand__dot"></span><span class="brand__name">Bluegate Lending Partners</span></div>
      <h1 class="headline">Is a Property Lien Putting <span>Your Home at Risk?</span></h1>
    </header>
    <div class="lien-band">HOA Liens • Tax Liens • Municipal Charges • Other Property-Related Liens</div>
    <div class="front__photo" role="img" aria-label="Photo of a worried couple sitting on a sofa"></div>
    <div class="front__copy">
      <p class="front__intro">You may have options to resolve outstanding liens and protect your home.</p>
      <h2 class="front__sub">A Refinance or Home Equity Line of Credit (HELOC) may help you:</h2>
      <ul class="checklist" style="color:var(--navy)">
        <li><svg class="tick"><use href="#tick"/></svg><span style="color:var(--ink)">Pay off qualifying liens</span></li>
        <li><svg class="tick"><use href="#tick"/></svg><span style="color:var(--ink)">Consolidate debt into one manageable payment</span></li>
        <li><svg class="tick"><use href="#tick"/></svg><span style="color:var(--ink)">Access your home's equity</span></li>
        <li><svg class="tick"><use href="#tick"/></svg><span style="color:var(--ink)">Improve your financial flexibility</span></li>
        <li><svg class="tick"><use href="#tick"/></svg><span style="color:var(--ink)">Avoid additional penalties, fees, or collection actions</span></li>
      </ul>
    </div>
    <div class="front__footer"></div>
    <div class="cta">
      <p class="cta__lead">Don't wait until the situation becomes more difficult.</p>
      <p class="cta__main">Call today for a confidential review of your options.</p>
    </div>
    <p class="front__contact">Bluegate Lending Partners, Inc. • (800) 647-2915 x 42 • www.bluegatelendco.com • NMLS #381640</p>
  </section>

  <section class="postcard postcard--back">
    <div class="back__photo" role="img" aria-label="Photo of a city skyline at sunset"></div>
    <div class="back__panel">
      <h2 class="back__title">Your Home Equity <span>Could Be the Solution</span></h2>
      <p class="back__lead">If you have received notices regarding:</p>
      <ul class="notices">
        <li>Delinquent Property Taxes</li>
        <li>HOA or Condo Association Assessments</li>
        <li>Municipal Utility Liens</li>
        <li>Special Assessments</li>
        <li>Other Property-Related Obligations</li>
      </ul>
      <p class="back__close">You may qualify for financing options designed to help satisfy those obligations and bring your property current.</p>
    </div>
    <div class="back__programs">
      <p class="programs__lead">Our experienced mortgage professionals can review your situation and discuss available programs, including:</p>
      <ul class="programs__grid">
        <li><svg class="tick"><use href="#tick"/></svg>Cash-Out Refinancing</li>
        <li><svg class="tick"><use href="#tick"/></svg>Home Equity Loans</li>
        <li><svg class="tick"><use href="#tick"/></svg>Home Equity Lines of Credit (HELOCs)</li>
        <li><svg class="tick"><use href="#tick"/></svg>Debt Consolidation Solutions</li>
      </ul>
    </div>
    <div class="back__contact-band"></div>
    <div class="headshot" role="img" aria-label="Portrait photo of loan officer Marcus Delaney"></div>
    <div class="contact">
      <p class="contact__lead">Contact Marcus Delaney today at</p>
      <p class="contact__phone"><svg width="11" height="12" viewBox="0 0 24 24" aria-hidden="true"><path fill="#fff" d="M6.6 10.8a15.1 15.1 0 006.6 6.6l2.2-2.2a1 1 0 011-.25 11.4 11.4 0 003.6.57 1 1 0 011 1V20a1 1 0 01-1 1A17 17 0 013 4a1 1 0 011-1h3.5a1 1 0 011 1c0 1.25.2 2.45.57 3.57a1 1 0 01-.25 1z"/></svg>(800) 647-2915 x42</p>
      <p class="contact__mail"><svg width="9" height="9" viewBox="0 0 12 12" aria-hidden="true"><circle cx="6" cy="6" r="6" fill="#fff"/><rect x="3" y="4" width="6" height="4" fill="none" stroke="#b8a53a" stroke-width="0.9"/><path d="M3 4l3 2.2L9 4" fill="none" stroke="#b8a53a" stroke-width="0.9"/></svg>mdelaney@bluegatelendco.com</p>
      <p class="contact__nmls">(NMLS #57308)</p>
    </div>
    <div class="badge">
      <p class="badge__free">FREE</p>
      <p class="badge__consult">CONSULTATION</p>
      <p class="badge__no">NO OBLIGATION</p>
    </div>
    <div class="back__mail-side">
      <div class="brand"><span class="brand__dot"></span><span class="brand__name">Bluegate Lending Partners</span></div>
      <div class="stamp-box"></div>
    </div>
  </section>
</body>
</html>
```